Lab & Medical Equipment Repair Company Business Card Design

Looking for business card design for a lab & medical equipment repair company. Must be double-sided and must list our primary pieces we repair. Optionally, can include a QR code which should direct to our website.

Clients are usually doctors, so the card must be designed with a professional tone; however, we are looking for creativity in presentation. Open as to what should be on the front and back on card.

** Looking for a CLEAN design with creativity. Please use "Nice to have Priorities" items with discretion.

Core marketing logic:

When lab or medical equipment needs repair, most doctors call the manufacturers and schedule a technician to repair. Usually this takes one or two weeks, and, often, their work spoils. Alternatively, the doctors could hold equipment insurance which gives them a less expensive cost, but the response time is still similarly long.

Our company provides both competitive rates and one of the fastest response times in the industry. Technicians are dispatched directly to the site of the equipment, usually within 24 hours. Equipment under contract receives the same fast response time and includes complimentary annual maintenance. We service some of the most prestigious facilities in the Pittsburgh area and cover all of Western Pennsylvania, Ohio, and West Virginia.

Target Market(s)

Laboratory owners (doctors)

Industry/Entity Type

Marketing

Requirements
Must have
• Company Logo
Employee Name: Ray Dunwoody
Employee Title: CEO
Company Phone: 724-555-0187
Company Fax: 866-555-0143
Company Address: PO Box 518 Harmony Glen, PA 16099
Company Website: www.brightfixlabtech.example
Equipment We Service: Freezers, Cryostorage, Incubators, Centrifuges, Refrigerators, Environmental Chambers, Autoclaves, and more.

Nice to have
• Company Facebook: facebook.com/bfltllc
Company Twitter: @BFLTLLC
QR Code (link to website): www.brightfixlabtech.example

```html
<!DOCTYPE html>
<html lang="en">
<head>
<meta charset="utf-8">
<title>BFLT Business Card – Front and Back</title>
<link href="https://fonts.googleapis.com/css2?family=Arimo:ital,wght@0,400;0,700;1,400&family=Cabin:wght@600&display=swap" rel="stylesheet">
<style>
  :root {
    --navy: #22223b;
    --green: #1fa04a;
    --white: #ffffff;
    --beige: #e6dcc0;
    --ink: #1b1b2a;
    --backdrop: #e7e4df;
  }
  * { box-sizing: border-box; margin: 0; padding: 0; }
  html, body {
    width: 1200px; height: 750px; overflow: hidden;
    background: var(--backdrop);
    font-family: "Arimo", Arial, sans-serif;
  }
  .sheet {
    position: relative; width: 1200px; height: 750px;
    display: flex; justify-content: center; align-items: center; gap: 40px;
  }
  .card {
    position: relative; width: 550px; height: 335px;
    background: var(--white); overflow: hidden;
    box-shadow: 0 4px 14px rgba(0,0,0,.22);
  }

  /* Front */
  .front__brand {
    position: absolute; left: 0; top: 0; width: 243px; height: 100%;
    background: var(--navy);
    display: flex; flex-direction: column; align-items: center; justify-content: center;
    padding-top: 6px;
  }
  .front__stripe {
    position: absolute; left: 243px; top: 0; width: 10px; height: 100%;
    background: var(--green);
  }
  .wordmark {
    display: flex; align-items: center; gap: 10px;
    font-family: "Arimo", Arial, sans-serif; font-weight: 700;
    letter-spacing: 2px;
  }
  .wordmark__square { width: 12px; height: 12px; background: var(--green); }
  .front .wordmark { font-size: 44px; color: var(--white); }
  .tagline {
    font-family: "Cabin", "Gill Sans", sans-serif; font-weight: 600;
    text-transform: uppercase; text-align: center; line-height: 1.3;
  }
  .front .tagline { margin-top: 16px; font-size: 14.5px; color: var(--beige); }

  .front__details {
    position: absolute; left: 253px; right: 0; top: 0; bottom: 0;
    text-align: right; padding-right: 17px;
  }
  .person__name {
    position: absolute; right: 17px; top: 140px;
    font-size: 26px; font-weight: 700; color: var(--navy);
  }
  .person__rule {
    position: absolute; left: 22px; right: 0; top: 174px;
    height: 1px; background: var(--green);
  }
  .person__title {
    position: absolute; right: 17px; top: 180px;
    font-size: 26px; font-style: italic; color: var(--ink);
  }
  .contact {
    position: absolute; right: 17px; top: 232px;
    list-style: none; font-size: 15.5px; line-height: 22px; color: var(--ink);
  }

  /* Back */
  .back__band { position: absolute; left: 0; width: 100%; background: var(--navy); }
  .back__band--top { top: 0; height: 93px; }
  .back__band--bottom {
    bottom: 0; height: 102px;
    color: var(--white); text-align: center;
    font-size: 15.5px; line-height: 20.5px; padding-top: 9px;
  }
  .back__logo {
    position: absolute; left: 0; right: 0; top: 93px; height: 140px;
    display: flex; flex-direction: column; align-items: center; justify-content: center;
  }
  .back .wordmark { font-size: 54px; color: var(--ink); }
  .back .tagline { margin-top: 12px; font-size: 15px; color: #333344; }
  .services__heading { font-weight: 700; }
</style>
</head>
<body>
<main class="sheet">
  <section class="card front" aria-label="Business card front">
    <div class="front__brand">
      <div class="wordmark"><span>BFLT</span><span class="wordmark__square"></span></div>
      <p class="tagline">Lab &amp; Medical Equipment<br>Repair</p>
    </div>
    <div class="front__stripe"></div>
    <div class="front__details">
      <h1 class="person__name">Ray Dunwoody</h1>
      <div class="person__rule"></div>
      <p class="person__title">CEO</p>
      <ul class="contact">
        <li>PO Box 518 Harmony Glen, PA 16099</li>
        <li>Phone: 724-555-0187</li>
        <li>Fax: 866-555-0143</li>
        <li>www.brightfixlabtech.example</li>
      </ul>
    </div>
  </section>

  <section class="card back" aria-label="Business card back">
    <div class="back__band back__band--top"></div>
    <div class="back__logo">
      <div class="wordmark"><span>BFLT</span><span class="wordmark__square"></span></div>
      <p class="tagline">Lab &amp; Medical Equipment Repair</p>
    </div>
    <div class="back__band back__band--bottom">
      <p class="services__heading">We Service:</p>
      <p>Freezers - Cryostorage - Incubators - Centrifuges - Refrigerators</p>
      <p>Environmental Chambers - Autoclaves</p>
      <p>and more ...</p>
    </div>
  </section>
</main>
</body>
</html>
```